Refresh web site from year 2003

Voltaro Works has a web site (https://vowrk-site.no/) from early 2000 that needs to be refreshed.

Attached are company logo, favicon files, a licensed image to be used, an animation that illustrate the use of one of the products.

Target Market(s)

Industrial customers

Industry/Entity Type

Electrical Switch Board Builders, Automation Industry

Coding

Coded - Design and coding required

Number of Pages Required

3 page

Requirements
Must have
• WordPress site. Use attached animation in the front page (source file is in Adobe Animation format, if adjustments are needed). Product page for two products, "KTR" and "QX-7 Ver B".
Nice to have
• The site should focus on promoting two products KTR and QX-7 Ver B.

```html
<!DOCTYPE html>
<html lang="en">
<head>
<meta charset="utf-8">
<title>Products – Voltaro Works</title>
<link rel="stylesheet" href="https://fonts.googleapis.com/css2?family=Lato:wght@400;700&family=Ubuntu:wght@400;500;700&display=swap">
<style>
:root{
  --brand:#004a80;
  --ink:#1f1f1f;
  --text:#555b61;
  --line:#d9dde2;
  --soft:#f3f5f8;
  --panel:#f5f5f5;
  --footer:#1c1c1c;
  --white:#ffffff;
}
*{margin:0;padding:0;box-sizing:border-box}
html,body{width:1200px;height:3122px;overflow:hidden}
body{position:relative;background:var(--white);font-family:"Lato",sans-serif;color:var(--text)}
.abs{position:absolute}
h1,h2,h3,h4{font-family:"Ubuntu",sans-serif;font-weight:500;color:var(--ink)}

/* header */
.site-header{left:0;top:0;width:1200px;height:118px;background:var(--white)}
.brand-name{left:111px;top:38px;font-family:"Ubuntu",sans-serif;font-weight:700;font-size:32px;color:var(--brand)}
.topline{right:111px;top:20px;font-size:18px;color:#222;display:flex;align-items:center;gap:8px}
.topline svg{fill:var(--brand)}
.nav{right:111px;top:63px;display:flex;gap:29px;font-family:"Ubuntu",sans-serif;font-size:19px;color:#111}
.nav .active{color:var(--brand)}

/* hero */
.hero{left:0;top:118px;width:1200px;height:311px;background:linear-gradient(90deg,#eeeeee 0%,#ececec 38%,#d9dadb 60%,#cfd1d2 80%,#dcdcdc 100%)}
.hero h1{position:absolute;left:109px;top:122px;font-size:60px;font-weight:700;color:#1a1a1a}

/* product intro */
.product-visual{left:111px;top:510px;width:490px;height:359px;background:var(--panel);box-shadow:0 4px 14px rgba(0,0,0,.12)}
.photo-fill{left:152px;top:577px;width:283px;height:181px;background:linear-gradient(90deg,#b9bec2,#e3e4e2 45%,#c9a98f 75%,#9c9e9f)}
.indicator-fill{left:492px;top:510px;width:66px;height:359px;background:linear-gradient(180deg,#e9e9e9,#5b5b5b 55%,#e9e9e9)}
.product-title{left:670px;top:505px;width:470px;font-size:35px;line-height:40px}
.ticks{list-style:none;font-size:17px;line-height:33.5px}
.ticks li{display:flex;align-items:flex-start;gap:10px}
.ticks svg{flex:none;margin-top:10px}
.features{left:670px;top:604px}
.desc{left:670px;top:754px;width:420px;font-size:17px;line-height:24px}
.desc h4{font-family:"Lato",sans-serif;font-weight:700;color:#333;font-size:17px}
.desc p{margin-bottom:24px}

/* application & specs */
.sec-title{font-size:23px}
.apps{left:114px;top:1412px;width:430px}
.apps .ticks{margin-top:16px;line-height:24px}
.apps .ticks li{margin-bottom:24px}
.specs{left:111px;top:1662px;width:440px}
.specs .ticks{margin-top:16px;line-height:24px}
.specs .ticks li{margin-bottom:24px}
.drawing-panel{left:595px;top:1400px;width:491px;height:572px;background:var(--panel);box-shadow:0 4px 14px rgba(0,0,0,.1)}
.panel-label{font-family:"Ubuntu",sans-serif;font-size:18px;color:#333;text-align:center;width:491px;left:595px}
.draw-fill{background:linear-gradient(180deg,#ebebeb,#dcdcdc)}

/* order information */
.order{left:0;top:2053px;width:1200px;height:670px;background:var(--soft)}
.order-title{left:0;top:2103px;width:1200px;text-align:center;font-size:26px}
.order-code{left:0;top:2153px;width:1200px;text-align:center;font-family:"Ubuntu",sans-serif;font-weight:500;font-size:21px;color:#222}
.code-table{border-collapse:collapse;background:var(--white);font-size:17px;text-align:center}
.code-table th{background:var(--brand);color:var(--white);font-family:"Ubuntu",sans-serif;font-weight:500;font-size:20px;height:58px;border:1px solid #6b8fb0}
.code-table td{height:52px;border:1px solid var(--line);color:#666}
.code-table .c1{width:110px}
.code-table .c2{width:187px}

/* footer */
.site-footer{left:0;top:2723px;width:1200px;height:399px;background:var(--footer);color:var(--white)}
.foot-brand{left:111px;top:2838px;font-family:"Ubuntu",sans-serif;font-weight:700;font-size:40px;color:var(--white)}
.foot-h{font-family:"Ubuntu",sans-serif;font-weight:500;font-size:20px;color:var(--white)}
.foot-links{list-style:none;font-size:17px;line-height:33px}
.contact-list{list-style:none;font-size:17px;line-height:20px}
.contact-list li{display:flex;gap:12px;margin-bottom:20px}
.contact-list svg{fill:var(--white);flex:none;margin-top:3px}
.social{display:flex;gap:8px}
.social span{width:40px;height:40px;border:1.5px solid var(--white);border-radius:50%}
.foot-rule{left:111px;top:3036px;width:978px;height:1px;background:#3a3a3a}
.copyright{left:0;top:3061px;width:1200px;text-align:center;font-size:17px}
</style>
</head>
<body>

<header class="site-header abs">
  <div class="brand-name abs">Voltaro Works</div>
  <div class="topline abs">
    <svg width="14" height="14" viewBox="0 0 24 24"><path d="M6.6 10.8a15 15 0 0 0 6.6 6.6l2.2-2.2a1 1 0 0 1 1-.25 11.4 11.4 0 0 0 3.6.57 1 1 0 0 1 1 1V20a1 1 0 0 1-1 1A17 17 0 0 1 3 4a1 1 0 0 1 1-1h3.5a1 1 0 0 1 1 1c0 1.25.2 2.45.57 3.57a1 1 0 0 1-.25 1z"/></svg>
    <span>+47 400 12 345</span><span>&nbsp;|&nbsp;</span>
    <svg width="18" height="14" viewBox="0 0 24 18"><path d="M0 0h24v2.5L12 10 0 2.5zM0 5l12 7.5L24 5v13H0z"/></svg>
    <span>post@voltaro-mail.no</span>
    <svg width="56" height="16" viewBox="0 0 56 16" style="margin-left:18px">
      <rect x="0" y="2" width="24" height="13" fill="#d52b1e"/><rect x="6" y="2" width="4" height="13" fill="#fff"/><rect x="0" y="6.5" width="24" height="4" fill="#fff"/><rect x="7" y="2" width="2" height="13" fill="#1d3f8f"/><rect x="0" y="7.5" width="24" height="2" fill="#1d3f8f"/>
      <rect x="30" y="2" width="24" height="13" fill="#2b3f8c"/><rect x="40" y="2" width="4" height="13" fill="#fff"/><rect x="30" y="6.5" width="24" height="4" fill="#fff"/><rect x="41" y="2" width="2" height="13" fill="#d52b1e"/><rect x="30" y="7.5" width="24" height="2" fill="#d52b1e"/>
    </svg>
  </div>
  <nav class="nav abs">
    <span>Home</span><span>About us</span><span>Services</span><span class="active">Products</span><span>Contact</span>
  </nav>
</header>

<section class="hero abs" role="img" aria-label="Photo of electrical switchboard cabinets with indicators and switches">
  <h1>Products</h1>
</section>

<div class="product-visual abs"></div>
<div class="photo-fill abs" role="img" aria-label="Photo of switchboard cabinets"></div>
<div class="indicator-fill abs" role="img" aria-label="Illustration of the switch position indicator on a circuit line"></div>

<h2 class="product-title abs">Switch position indicator with light Type KTR</h2>

<ul class="ticks features abs">
  <li><svg width="14" height="14" viewBox="0 0 14 14"><circle cx="7" cy="7" r="7" fill="#004a80"/><path d="M3.8 7.2l2.2 2.1 4.2-4.4" stroke="#fff" stroke-width="1.8" fill="none"/></svg>Very long operating time due to the LED</li>
  <li><svg width="14" height="14" viewBox="0 0 14 14"><circle cx="7" cy="7" r="7" fill="#004a80"/><path d="M3.8 7.2l2.2 2.1 4.2-4.4" stroke="#fff" stroke-width="1.8" fill="none"/></svg>Easy mounting</li>
  <li><svg width="14" height="14" viewBox="0 0 14 14"><circle cx="7" cy="7" r="7" fill="#004a80"/><path d="M3.8 7.2l2.2 2.1 4.2-4.4" stroke="#fff" stroke-width="1.8" fill="none"/></svg>Reliable reading at long distance</li>
  <li><svg width="14" height="14" viewBox="0 0 14 14"><circle cx="7" cy="7" r="7" fill="#004a80"/><path d="M3.8 7.2l2.2 2.1 4.2-4.4" stroke="#fff" stroke-width="1.8" fill="none"/></svg>Wide angle</li>
</ul>

<div class="desc abs">
  <h4>Application</h4>
  <p>The indicator is used in switchboards and control cabi-<br>nets to display switch positions,<br>valve positions, etc. for easy reading.</p>
  <h4>Structure and operation</h4>
  <p>The indicator consists of two rows of lights, one show-<br>ing vertical and the other showing horizontal direction.<br>Green vertical row of LEDs shows switch etc. in: On po-<br>sition .<br>Red horizontal row of LEDs shows switch etc. in: Off<br>position.</p>
  <h4>Other information</h4>
  <p>Recess for the indicator and the locking cam are shown<br>in the figure below.<br>The indicator is delivered in a standard round design.<br>Loose square front included for circuit breaker.<br>Other colors and combinations of light strips can be<br>supplied on request.<br>The green or red light indicates switch positions in a<br>way that makes it<br>possible to read switch positions at a distance of 20<br>meters and at an angle of ± 45 °.</p>
</div>

<div class="apps abs">
  <h3 class="sec-title">Areas Of Application</h3>
  <ul class="ticks">
    <li><svg width="14" height="14" viewBox="0 0 14 14"><circle cx="7" cy="7" r="7" fill="#004a80"/><path d="M3.8 7.2l2.2 2.1 4.2-4.4" stroke="#fff" stroke-width="1.8" fill="none"/></svg><span>The indicator works with both AC or DC voltage.</span></li>
    <li><svg width="14" height="14" viewBox="0 0 14 14"><circle cx="7" cy="7" r="7" fill="#004a80"/><path d="M3.8 7.2l2.2 2.1 4.2-4.4" stroke="#fff" stroke-width="1.8" fill="none"/></svg><span>Available supply: 24V ..... .110V ..... ..230V ac / dc<br>(other voltages on request.)</span></li>
    <li><svg width="14" height="14" viewBox="0 0 14 14"><circle cx="7" cy="7" r="7" fill="#004a80"/><path d="M3.8 7.2l2.2 2.1 4.2-4.4" stroke="#fff" stroke-width="1.8" fill="none"/></svg><span>For easy connection, the indicator has a pluggable<br>base with 3 screw connections. (See figure below)</span></li>
  </ul>
</div>

<div class="specs abs">
  <h3 class="sec-title">Technical specifications</h3>
  <ul class="ticks">
    <li><svg width="14" height="14" viewBox="0 0 14 14"><circle cx="7" cy="7" r="7" fill="#004a80"/><path d="M3.8 7.2l2.2 2.1 4.2-4.4" stroke="#fff" stroke-width="1.8" fill="none"/></svg><span>Power: Approx. 12mA in the specified voltage range.</span></li>
    <li><svg width="14" height="14" viewBox="0 0 14 14"><circle cx="7" cy="7" r="7" fill="#004a80"/><path d="M3.8 7.2l2.2 2.1 4.2-4.4" stroke="#fff" stroke-width="1.8" fill="none"/></svg><span>Working temperatures: -40 to + 70 ° C</span></li>
    <li><svg width="14" height="14" viewBox="0 0 14 14"><circle cx="7" cy="7" r="7" fill="#004a80"/><path d="M3.8 7.2l2.2 2.1 4.2-4.4" stroke="#fff" stroke-width="1.8" fill="none"/></svg><span>Enclosure: IP65</span></li>
  </ul>
</div>

<div class="drawing-panel abs"></div>
<div class="panel-label abs" style="top:1419px">Dimensions</div>
<div class="draw-fill abs" style="left:742px;top:1460px;width:203px;height:110px" role="img" aria-label="Technical drawing of indicator dimensions and panel cut-out"></div>
<div class="panel-label abs" style="top:1599px">Assembly</div>
<div class="draw-fill abs" style="left:658px;top:1642px;width:375px;height:109px" role="img" aria-label="Drawing of hands assembling the indicator into a panel"></div>
<div class="panel-label abs" style="top:1771px">Wiring diagram Connection with pluggable base.</div>
<div class="draw-fill abs" style="left:685px;top:1818px;width:315px;height:122px" role="img" aria-label="Wiring diagram of the three-terminal pluggable base with connection table"></div>

<section class="order abs"></section>
<h2 class="order-title abs">Order information</h2>
<div class="order-code abs">KTR-110-G-R-SQ</div>

<svg class="abs" style="left:0;top:2180px" width="1200" height="360" viewBox="0 2180 1200 360">
  <g stroke="#004a80" stroke-width="3">
    <line x1="559" y1="2186" x2="588" y2="2186"/>
    <line x1="599" y1="2186" x2="621" y2="2186"/>
    <line x1="625" y1="2186" x2="645" y2="2186"/>
    <line x1="651" y1="2186" x2="678" y2="2186"/>
  </g>
  <g stroke="#5c7f9f" stroke-width="1.2" fill="none">
    <polyline points="572,2190 572,2276 516,2276"/>
    <polyline points="607,2190 607,2525 516,2525"/>
    <polyline points="635,2190 635,2525 720,2525"/>
    <polyline points="663,2190 663,2276 720,2276"/>
  </g>
</svg>

<table class="code-table abs" style="left:219px;top:2245px">
  <tr><th class="c1">Code</th><th class="c2">[Voltage]</th></tr>
  <tr><td>24</td><td>24 V ac/dc</td></tr>
  <tr><td>110</td><td>110 V ac/dc</td></tr>
  <tr><td>11</td><td>230 V ac/dc</td></tr>
</table>
<table class="code-table abs" style="left:720px;top:2245px">
  <tr><th class="c1">Code</th><th class="c2">[Accessories]</th></tr>
  <tr><td>SQ</td><td>Square frame</td></tr>
  <tr><td>SH</td><td>Sign holder</td></tr>
  <tr><td>N</td><td>None</td></tr>
</table>
<table class="code-table abs" style="left:219px;top:2493px">
  <tr><th class="c1">Code</th><th class="c2">[Vertical LED row]</th></tr>
  <tr><td>G</td><td>Green Color</td></tr>
  <tr><td>C1</td><td>Custom Color 1</td></tr>
</table>
<table class="code-table abs" style="left:720px;top:2493px">
  <tr><th class="c1">Code</th><th class="c2">[Horizontal LED row]</th></tr>
  <tr><td>R</td><td>Red Color</td></tr>
  <tr><td>C2</td><td>Custom Color 2</td></tr>
</table>

<footer class="site-footer abs"></footer>
<div class="foot-brand abs">Voltaro Works</div>

<div class="abs" style="left:456px;top:2770px">
  <div class="foot-h">Quick Links</div>
  <ul class="foot-links" style="margin-top:16px">
    <li>Home</li><li>About us</li><li>Services</li><li>Products</li><li>Contact</li>
  </ul>
</div>

<div class="abs" style="left:639px;top:2770px;color:#fff">
  <div class="foot-h">Contact Us</div>
  <ul class="contact-list" style="margin-top:24px">
    <li><svg width="12" height="16" viewBox="0 0 12 16"><path d="M6 0a6 6 0 0 1 6 6c0 4.5-6 10-6 10S0 10.5 0 6a6 6 0 0 1 6-6zm0 3.5a2.5 2.5 0 1 0 0 5 2.5 2.5 0 0 0 0-5z"/></svg><span>Fjordvegen 12<br>N-4600 Bakkeby<br>Norway</span></li>
    <li><svg width="14" height="14" viewBox="0 0 24 24"><path d="M6.6 10.8a15 15 0 0 0 6.6 6.6l2.2-2.2a1 1 0 0 1 1-.25 11.4 11.4 0 0 0 3.6.57 1 1 0 0 1 1 1V20a1 1 0 0 1-1 1A17 17 0 0 1 3 4a1 1 0 0 1 1-1h3.5a1 1 0 0 1 1 1c0 1.25.2 2.45.57 3.57a1 1 0 0 1-.25 1z"/></svg><span>+47 400 12 345</span></li>
    <li><svg width="16" height="13" viewBox="0 0 24 18"><path d="M0 0h24v2.5L12 10 0 2.5zM0 5l12 7.5L24 5v13H0z"/></svg><span>post@voltaro-mail.no</span></li>
    <li><svg width="14" height="14" viewBox="0 0 14 14"><circle cx="7" cy="7" r="6" fill="none" stroke="#fff" stroke-width="1.6"/><path d="M1 7h12M7 1c-3 3.5-3 8.5 0 12M7 1c3 3.5 3 8.5 0 12" stroke="#fff" stroke-width="1.2" fill="none"/></svg><span>www.vowrk-site.no</span></li>
  </ul>
</div>

<div class="abs" style="left:896px;top:2770px">
  <div class="foot-h">Social Media</div>
  <div class="social" style="margin-top:24px"><span></span><span></span><span></span></div>
</div>

<div class="foot-rule abs"></div>
<div class="copyright abs" style="color:#fff">Copyright © 2003-2021 Voltaro Works.</div>

</body>
</html>
```